Small animal veterinary clinic needs a new web site design

We need a new web site design for Harlowe Veterinary Clinic. The clinic performs medicine, surgery, and wellness care for cats and dogs. We have been in business for over 50 years so we want to project stability, reliability, class, elegance, and professionalism. We also want to convey that we have modern facilities and services and perform high quality medicine.
The current web site has been in place for many years and looks stale but for reference it is at http://www.harlowevetcare.example. We will be re-writing most of the content and looking to add additional pages, videos, downloadable documents (forms, brochures, marketing materials, etc.) The new owners prefer a more classy, modern look. Some vet clinic sites we like are http://pintrelpaws.example and http://corvalanimalcare.example. We like a nice, clean, fresh, interactive interface.
Our new logo is attached. We want the color scheme of the web site to be complementary to the colors in the logo, especially the blue and green. The purple color of the text should just be used for accent. Upon request and if necessary, I can supply the Adobe Illustrator source file for the logo.
We are looking for a set of page designs - a great, eye-catching home page and 2-3 content page layouts we can use to create content pages with our own text and other content. Navigation design is very important as well. Again, we can fill in the content of the navigation links but I would like a nice, easy-to-use, logical navigation design. If you want some content or navigation links to use as reference during your design phase, feel free to pull whatever content or navigation you want from our existing web site. I am not looking for just images, I would like actual page files - HTML, CSS, etc.
Thanks and good luck!
Target Market(s)
We cater to pet owners across a wide age range. Socio-economic status of our customers is middle class and above. We do not target price shoppers.
Industry/Entity Type
Veterinary
Colors
Designer to choose colors to be used in the design.
Requirements
Must have
- Must look professional, clean, and modern. We are looking for simple but elegant design and navigation. 1 home page design, 2-3 content page designs delivered with code (HTML & CSS).
Nice to have
- When HTML/CSS is delivered, it would be awesome if it were mobile ready as well.
Should not have
- Colors that are too bold. Layout that is too complex.

```html
<!DOCTYPE html>
<html lang="en">
<head>
<meta charset="utf-8">
<title>Harlowe Veterinary Clinic</title>
<link href="https://fonts.googleapis.com/css2?family=Arimo:wght@400;700&display=swap" rel="stylesheet">
<style>
:root{
  --navy:#0b3468;
  --band-top:#4f8bc8;
  --band-bottom:#0d3d75;
  --tab-blue:#4a89c8;
  --link-blue:#2f6fb3;
  --green:#5cb85c;
  --green-frame:#4cae4c;
  --panel:#eeeeee;
  --line:#c9d3de;
  --text:#555a60;
  --white:#ffffff;
  --brand-ink:#3b3a78;
  --brand-dot:#1f8f9a;
}
*{box-sizing:border-box;margin:0;padding:0}
html,body{width:1108px;height:1200px;overflow:hidden}
body{position:relative;background:var(--white);font-family:"Arimo",Arial,sans-serif;color:var(--text)}
a{text-decoration:none}

.band{position:absolute;left:0;top:110px;width:1108px;height:535px;border-top:3px solid #d5dbe2;
  background:linear-gradient(180deg,var(--band-top) 0%,#1f5a98 45%,var(--band-bottom) 100%)}

.brand{position:absolute;left:42px;top:15px;width:235px;height:215px;background:var(--white);border:1px solid #ccd;
  display:flex;flex-direction:column;align-items:center;justify-content:center;gap:12px}
.brand-mark{width:26px;height:26px;border-radius:50%;background:var(--brand-dot)}
.brand-name{font-size:19px;font-weight:700;color:var(--brand-ink);line-height:1.25;text-align:center;width:190px}

.contact{position:absolute;left:42px;top:274px;width:240px;color:var(--white)}
.contact h2{font-size:23px;font-weight:400;margin-bottom:10px}
.contact p{font-size:12px;font-weight:700;line-height:15px}

.social{position:absolute;left:42px;top:417px;display:flex;gap:27px}
.social-link{width:40px;height:40px;border-radius:4px;display:flex;align-items:center;justify-content:center;
  color:var(--white);font-size:9px;font-weight:700;box-shadow:0 1px 2px rgba(0,0,0,.3)}
.social-kinly{background:#3b5b9a}
.social-gathr{background:#d3463a}
.social-peeple{background:#3fa9e0}
.social-vidra{background:#c4302b}

.cta{position:absolute;left:42px;width:235px;height:38px;background:var(--green);border-radius:4px;color:var(--white);
  font-size:13px;font-weight:700;display:flex;align-items:center;justify-content:center;border:1px solid #4a9d4a}

.nav{position:absolute;left:306px;top:13px;width:767px;height:36px;display:flex;list-style:none}
.nav li{flex:1;display:flex;align-items:center;justify-content:center;font-size:13px;color:var(--link-blue)}
.nav li.active{background:var(--tab-blue);color:var(--white);font-weight:700;border-radius:3px}

.slider{position:absolute;left:306px;top:60px;width:767px;height:339px;border:7px solid var(--green-frame);
  background:
    radial-gradient(ellipse 22% 38% at 50% 52%,#efe9e2 0%,#cfc4b4 45%,rgba(150,130,95,0) 100%),
    linear-gradient(100deg,#1b2410 0%,#3c4a22 25%,#6a6430 50%,#3e4a20 75%,#182010 100%)}
.slider .arrow{position:absolute;top:146px}

.content{position:absolute;left:306px;top:426px;width:767px;height:640px;border:9px solid var(--navy);background:var(--panel)}
.welcome{position:absolute;left:55px;top:58px;font-size:16px;font-weight:400;color:#555}
.welcome-photo{position:absolute;left:55px;top:80px;width:194px;height:120px;
  background:linear-gradient(90deg,#b48a6a 0%,#d9c0a5 35%,#efe4cf 60%,#c8b090 100%)}
.intro{position:absolute;left:278px;top:84px;width:412px;font-size:11.5px;line-height:16px;color:#6a6f75}
.intro a{color:var(--link-blue)}

.video{position:absolute;left:55px;top:218px;width:642px;height:359px;
  background:linear-gradient(180deg,#c6a678 0%,#b0875c 45%,#e6e2dc 75%,#f4f2ef 100%)}
.video-title{position:absolute;left:0;top:0;width:100%;height:26px;background:rgba(20,20,20,.75);color:var(--white);font-size:12px;font-weight:700;padding:6px 10px}
.play{position:absolute;left:291px;top:150px;width:60px;height:44px;background:rgba(30,30,30,.88);border-radius:8px}
.controls{position:absolute;left:0;bottom:0;width:100%;height:24px;background:#1b1b1b;color:#ddd;font-size:10px;display:flex;align-items:center;gap:14px;padding:0 10px}
.controls .time{margin-right:auto}

.widget{position:absolute;background:var(--white);border:1px solid #8aa4c0}
.widget h3{height:34px;background:var(--tab-blue);color:var(--white);font-size:12px;font-weight:700;padding:10px 14px}
.news{left:42px;top:664px;width:235px;height:281px}
.news ul{list-style:none;margin:18px 14px}
.news li{height:39px;border:1px solid var(--line);border-top:none;font-size:12px;color:#444;display:flex;align-items:center;padding-left:12px;gap:6px}
.news li:first-child{border-top:1px solid var(--line)}
.example{left:42px;top:965px;width:235px;height:87px}
.example p{margin:14px 16px;color:#aaa;font-size:12px}
.services{left:42px;top:1091px;width:326px;height:140px}
.services ul{list-style:none;margin:18px 14px}
.services li{height:36px;border:1px solid var(--line);font-size:12px;display:flex;align-items:center;padding-left:12px;gap:6px;color:#444}
.staff{left:395px;top:1091px;width:327px;height:140px}
.staff-photo{position:absolute;top:52px;width:72px;height:72px;border:1px solid #bbb;padding:3px;background:var(--white)}
.staff-photo span{display:block;width:100%;height:100%;background:linear-gradient(180deg,#a9b39a 0%,#7d7a62 55%,#3e3a36 100%)}
.hours{left:749px;top:1091px;width:326px;height:140px}
.hours p{margin:28px 14px 0;font-size:12px;line-height:19px;color:#444}
</style>
</head>
<body>
<div class="band"></div>

<header class="brand"><span class="brand-mark"></span><span class="brand-name">Harlowe Veterinary Clinic</span></header>

<section class="contact">
  <h2>Get In touch With Us</h2>
  <p>Harlowe Veterinary<br>2280 Alder Crest Road<br>Brookhaven, SC 29410<br>Phone: (555) 014-2261<br>Fax: (555) 014-2278</p>
</section>

<nav class="social">
  <a class="social-link social-kinly">Kinly</a>
  <a class="social-link social-gathr">Gathr</a>
  <a class="social-link social-peeple">Peeple</a>
  <a class="social-link social-vidra">Vidra</a>
</nav>

<a class="cta" style="top:477px">Schedule an Appointment Today</a>
<a class="cta" style="top:533px">Make a Reservation Today</a>

<ul class="nav">
  <li class="active">Home</li><li>Services</li><li>Our Staff</li><li>Care Guides</li><li>Contact us</li>
</ul>

<section class="slider" role="img" aria-label="Slide photo of a white and grey kitten sitting outdoors">
  <svg class="arrow" style="left:22px" width="20" height="28" viewBox="0 0 20 28"><path d="M15 3 4 14l11 11" fill="none" stroke="#ddd" stroke-width="4"/></svg>
  <svg class="arrow" style="right:22px" width="20" height="28" viewBox="0 0 20 28"><path d="M5 3l11 11L5 25" fill="none" stroke="#fff" stroke-width="4"/></svg>
</section>

<main class="content">
  <h1 class="welcome">Welcome to HARLOWE</h1>
  <div class="welcome-photo" role="img" aria-label="Photo of a child hugging a yellow labrador"></div>
  <p class="intro">Harlowe Veterinary Clinic is a full-service veterinary medical hospital, located in Brookhaven, SC. The professional and courteous staff at Harlowe Veterinary Clinic seeks to provide the best possible medical care, surgical care and dental care for their highly-valued...<a>Read more</a></p>
  <div class="video" role="img" aria-label="Video still of a dog resting beside a sleeping baby">
    <div class="video-title">Cats and dogs meeting babies for the first time...</div>
    <div class="play"><svg width="60" height="44" viewBox="0 0 60 44"><path d="M24 14v16l13-8z" fill="#fff"/></svg></div>
    <div class="controls">
      <svg width="10" height="12" viewBox="0 0 10 12"><path d="M1 1v10l8-5z" fill="#ccc"/></svg>
      <svg width="14" height="12" viewBox="0 0 14 12"><path d="M1 4h3l4-3v10L4 8H1z" fill="#ccc"/><path d="M10 3q3 3 0 6" fill="none" stroke="#ccc" stroke-width="1.3"/></svg>
      <span class="time">0:00 / 3:33</span>
      <svg width="12" height="12" viewBox="0 0 12 12"><path d="M1 4V1h3M8 1h3v3M11 8v3H8M4 11H1V8" fill="none" stroke="#ccc" stroke-width="1.5"/></svg>
    </div>
  </div>
</main>

<aside class="widget news">
  <h3>latest news</h3>
  <ul>
    <li>&#9829; We Offer Pet Portals!</li>
    <li>&#9829; News Example 1</li>
    <li>&#9829; News Example 2</li>
    <li>&#9829; News Example 3</li>
    <li>&#9829; News Example 4</li>
  </ul>
</aside>

<aside class="widget example"><h3>Example Content Area</h3><p>——</p></aside>

<section class="widget services"><h3>Our Services</h3><ul><li>&#9829; Bathing</li></ul></section>

<section class="widget staff"><h3>Our Staff</h3>
  <div class="staff-photo" style="left:17px" role="img" aria-label="Staff portrait"><span></span></div>
  <div class="staff-photo" style="left:124px" role="img" aria-label="Staff portrait"><span></span></div>
  <div class="staff-photo" style="left:231px" role="img" aria-label="Staff portrait"><span></span></div>
</section>

<section class="widget hours"><h3>Opening Hours</h3>
  <p>Mon-Fri: 8:00am - 5:30pm<br>Sat: 8:00am - 11:30am<br>Sun: Closed</p>
</section>
</body>
</html>
```